Website Design for Mango Creek Cabins Hotel

Hi,

I am looking for a good 'web designer' to design me a website for a hotel I manage in Thailand. I own a web development company in Australia so the winner of the contest will be given regular work in the future. I have used a few designers from taskvoro and have had a few problems.

1. Understand Web development limitation.
As well as looking for someone who is creative at the same time I am looking for a designer who has a lot of web design experience and understands the limitations of web development.

2. Understands the English Language
I am looking for someone who understands English language very well. I have had problems in the past where designers don't understand the requirements due to their lack of understanding of the English Language. Please only enter the contest if your are very confidant with the English Language.

Contest Details.....

I need a LOGO & WEBSITE designing for a hotel on Phi Phi Island in Thailand (Mango Creek Cabins). I have a pixelnest page and am also advertised in [login to view URL] if you need any more information about the hotel. Phi Phi Island is a very beautiful place and there is so many nice images available on the internet.

Pages I need

1. Homepage
I want this to look very attractive with some general photos of Phi Phi Island and a combination of the best photos I have of the hotel. I will also want to add a little content in here about the hotel. This page will also have a menu displaying all the main pages. Home, Rooms & Accommodation, Facilities & More, Room Rates, Make a Booking, Contact & Map

2. Rooms & Accommodation
I want this page to have content about the rooms. I also want a selection of the best photos of the rooms on here. Please also add a link / button at the bottom of the page for 'book now' and 'check rates'.

3. Facilities & More
This page will have 4 sections. (Pool, Bar, Dining, Trips & Parties)
Please add a little bit of content about each section along with a selection of the best photos I have. Either all on one page or if you want to separate these out into separate pages and have a sub menu then this is ok too.

4. Room Rates,
This will be just a table showing the different room types, different seasons, and the prices. I have attached an image taken from another website as an example.

There are 3 seasons - Low, High, Peak
There are 6 room types - Double (Fan), Double(A/C), Twin (Fan), Twin (A/C), Triple (Fan), Triple (A/C)

5. Booking Form
Just a simple booking form. Because users can book a number of rooms then I need a form so the user can select the first room. There needs to be an 'add to booking'. The add to booking button will add this to the booking summary which will be on the same page as the form. This means that the user will able able to add more than one room under the same booking. At the end of the booking then there will be a 'submit booking' button which then sends the booking summery to mango creek cabins.

Fields
Booking Details Section
Firstname: textbox
Lastname: textbox
Nationality: textbox
Email Address: textbox
Additional Information: textarea

Rooms Section
Room Type: dropdown
Check-in Date: textbox
Duration (Nights): dropdown
ADD TO BOOKING BUTTON

Booking Summery Section
Room Type:
Check-In Date:
Number of Nights:
Room Cost:
Sub Total:
Total:
SUBMIT BOOKING BUTTON

6. Contact & Map
Just a basic contact page with...
Address, Phone, Email
Contact Form (Firstname (textbox), Lastname (textbox), Email (textbox), Enquiry (textarea)
Map - I have attached a simple example map you can use

I have attached a lot of images I have of the hotel. Please use the ones you think look good. I will leave the logo and website design / style up to you. I am hoping you are more creative then me anyway. I have also attached a read me text file which has some example sites and other details in there. Please read this. The only requirement i have is

```html
<!DOCTYPE html>
<html lang="en">
<head>
<meta charset="utf-8">
<title>Mango Creek Cabins</title>
<link href="https://fonts.googleapis.com/css2?family=Kaushan+Script&family=Open+Sans:wght@400;600&family=Ubuntu:wght@400;500&display=swap" rel="stylesheet">
<style>
:root{
  --sky-top:#2f8fe0;
  --sky-mid:#7cc2f2;
  --pool:#3aa6e0;
  --pool-deep:#1f7fc4;
  --panel:#f7f7f7;
  --olive:#7d8c1e;
  --ink:#2b2b2b;
  --text:#3c3c3c;
  --nav-top:#5aa8e6;
  --nav-bot:#2f7fc8;
  --navy:#0f5b94;
  --caption:rgba(235,235,235,.85);
  --slide-green:#3fae8d;
  --arrow:#0f3d1f;
}
*{box-sizing:border-box;margin:0;padding:0}
html,body{width:1200px;height:1067px;overflow:hidden}
body{position:relative;font-family:"Open Sans",Arial,sans-serif;color:var(--text)}
.backdrop{position:absolute;inset:0;
  background:linear-gradient(180deg,var(--sky-top) 0%,var(--sky-mid) 55%,#d8eef9 64%,var(--pool) 68%,var(--pool-deep) 100%)}
.page{position:absolute;left:273px;top:20px;width:654px;height:1000px;background:var(--panel);border-radius:8px;box-shadow:0 0 12px rgba(0,0,0,.25)}
.abs{position:absolute}
.logo{left:16px;top:16px;font-family:"Ubuntu",sans-serif;font-weight:500;font-size:28px;color:var(--olive);white-space:nowrap}
.tagline{left:86px;top:54px;font-family:"Ubuntu",sans-serif;font-size:11px;color:#1e1e1e;white-space:nowrap}
.contact{right:12px;font-size:12px;color:#333;display:flex;align-items:center;gap:6px;white-space:nowrap}
.contact.phone{top:26px}
.contact.mail{top:50px}
.nav{left:7px;top:91px;width:640px;height:29px;background:linear-gradient(var(--nav-top),var(--nav-bot));display:flex;border-radius:2px}
.nav a{color:#fff;text-decoration:none;font-size:9.5px;text-transform:uppercase;display:flex;align-items:center;justify-content:center;border-right:1px solid rgba(255,255,255,.35);white-space:nowrap}
.nav a:last-child{border-right:0}
.slider{left:7px;top:120px;width:640px;height:333px;background:linear-gradient(135deg,#4fc3a0 0%,var(--slide-green) 45%,#e9e9e9 70%,#6b4a2a 100%)}
.slide-arrow{top:168px;width:28px;height:40px;background:var(--arrow);display:flex;align-items:center;justify-content:center}
.slide-arrow.prev{left:0}
.slide-arrow.next{right:0}
.caption{left:7px;top:280px;width:346px;height:47px;background:var(--caption);padding:7px 10px;font-size:12px;line-height:16px;color:#222;text-transform:uppercase}
.welcome{left:0;width:654px;top:467px;text-align:center;font-family:"Kaushan Script",cursive;font-weight:400;font-size:20px;color:#1f1f1f}
.dots{left:167px;top:509px;width:320px;border-top:2px dotted #333}
.intro{left:50px;top:524px;width:554px;text-align:center;font-size:10.5px;line-height:16.5px;color:#333}
.btn{top:609px;height:34px;border-radius:17px;border:1px solid #bbb;background:linear-gradient(#fff,#ddd);box-shadow:0 2px 3px rgba(0,0,0,.25);font-family:"Ubuntu",sans-serif;font-size:13px;color:#222;display:flex;align-items:center;justify-content:center;white-space:nowrap}
.btn.tour{left:212px;width:107px}
.btn.book{left:327px;width:108px}
.divider{left:60px;top:669px;width:534px;height:6px;background:radial-gradient(ellipse at center,rgba(0,0,0,.18),transparent 70%)}
.feature{top:704px;width:199px;text-align:center}
.feature .photo{height:115px}
.feature h3{margin-top:10px;font-family:"Ubuntu",sans-serif;font-weight:400;font-size:12px;color:#333;text-transform:uppercase}
.feature .sub{font-family:"Kaushan Script",cursive;font-size:11px;color:#222;margin-top:1px}
.feature p{font-size:9px;line-height:13px;color:#333;margin:5px 2px 0}
.details{display:inline-block;margin-top:12px;width:71px;height:27px;line-height:27px;border-radius:5px;background:var(--navy);color:#fff;font-family:"Ubuntu",sans-serif;font-size:13px}
.f1{left:11px}.f2{left:227px}.f3{left:444px}
.food{background:linear-gradient(135deg,#6b5a3a,#c9a070,#3e3020)}
.pool{background:linear-gradient(180deg,#6a8a4a 0%,#3f7fb0 50%,#2a6fa8 100%)}
.party{background:linear-gradient(135deg,#2a1f18,#7a5a48,#1b1410)}
.footer{left:280px;top:1030px;font-size:9.5px;line-height:13px;color:#fff}
.social{top:1032px;display:flex;gap:9px;left:805px}
.social span{width:22px;height:22px;border-radius:50%;background:#fff;opacity:.95}
</style>
</head>
<body>
<div class="backdrop" role="img" aria-label="Tropical pool with palm trees under a blue sky"></div>

<main class="page">
  <div class="abs logo">Mango Creek Cabins</div>
  <div class="abs tagline">make your holydays Phi Phi island</div>
  <div class="abs contact phone">
    <svg width="14" height="12" viewBox="0 0 14 12"><path d="M1 4c0-2 3-3 6-3s6 1 6 3v1h-3V4H4v1H1z M3 6h8l1 5H2z" fill="#555"/></svg>
    +66(0) 555 010 277
  </div>
  <div class="abs contact mail">
    <svg width="14" height="10" viewBox="0 0 14 10"><rect x="0.5" y="0.5" width="13" height="9" fill="#666"/><path d="M1 1l6 5 6-5" stroke="#eee" fill="none"/></svg>
    info@mangocreekcabins.example
  </div>

  <nav class="abs nav">
    <a style="width:64px">Home</a>
    <a style="width:164px">Rooms &amp; Accommodation</a>
    <a style="width:93px">Facilities</a>
    <a style="width:94px">Room Rates</a>
    <a style="width:112px">Booking Form</a>
    <a style="width:113px">Contact &amp; Map</a>
  </nav>

  <section class="abs slider" role="img" aria-label="Twin-bed room with green walls">
    <div class="abs slide-arrow prev"><svg width="10" height="14"><path d="M8 1L2 7l6 6" stroke="#fff" stroke-width="2" fill="none"/></svg></div>
    <div class="abs slide-arrow next"><svg width="10" height="14"><path d="M2 1l6 6-6 6" stroke="#fff" stroke-width="2" fill="none"/></svg></div>
    <div class="abs caption">Lorem ipsum dolor sit amet, consectetuer adipiscing elit</div>
  </section>

  <h1 class="abs welcome">Welcome to Mango Creek Cabins</h1>
  <div class="abs dots"></div>
  <p class="abs intro">Lorem ipsum dolor sit amet, consectetuer adipiscing elit. Aenean commodo ligula eget dolor. Aenean massa. Cum sociis natoque penatibus et magnis dis parturient montes, nascetur ridiculus mus. Donec quam felis, ultricies nec, pellentesque eu, pretium quis, sem. Nulla consequat massa quis enim.Donec pede justo, fringilla vel, aliquet nec, vulputate eget, arcu.</p>
  <div class="abs btn tour">Take a Tour</div>
  <div class="abs btn book">Request Booking</div>
  <div class="abs divider"></div>

  <article class="abs feature f1">
    <div class="photo food" role="img" aria-label="Guests dining together at a long table"></div>
    <h3>Delicious Food Menu</h3>
    <div class="sub">Lorem ipsum dolor sit amet</div>
    <p>Lorem ipsum dolor sit amet, consectetuer adipiscing elit. Aenean commodo ligula eget dolor. Aenean massa. Cum sociis natoque penatibus et magnis dis parturient montes, nascetur ridiculus mus.</p>
    <span class="details">Details</span>
  </article>
  <article class="abs feature f2">
    <div class="photo pool" role="img" aria-label="Swimming pool with sun loungers and bar"></div>
    <h3>Attractive Pool &amp; Bar</h3>
    <div class="sub">Lorem ipsum dolor sit amet</div>
    <p>Lorem ipsum dolor sit amet, consectetuer adipiscing elit. Aenean commodo ligula eget dolor. Aenean massa. Cum sociis natoque penatibus et magnis dis parturient montes, nascetur ridiculus mus.</p>
    <span class="details">Details</span>
  </article>
  <article class="abs feature f3">
    <div class="photo party" role="img" aria-label="Night party with guests"></div>
    <h3>Trips &amp; Parties</h3>
    <div class="sub">Lorem ipsum dolor sit amet</div>
    <p>Lorem ipsum dolor sit amet, consectetuer adipiscing elit. Aenean commodo ligula eget dolor. Aenean massa. Cum sociis natoque penatibus et magnis dis parturient montes, nascetur ridiculus mus.</p>
    <span class="details">Details</span>
  </article>
</main>

<footer>
  <div class="abs footer">Copyright © 2013 Mango Creek Cabins . All Rights Reserved.</div>
  <div class="abs social"><span></span><span></span><span></span><span></span></div>
</footer>
</body>
</html>
```